Heronfield Wealth Advisors, Inc. Marketing Collateral - 401k Rollover Decisions

We are looking to create a branded one-pager marketing collateral piece talking about 401k Rollovers & the important information people should know. Rough draft of concept & content included below, and we will finalize copy later. Would include a call to action to contact us. Our website and other contact information are available at https://growwithheronfield.com/.

Target Market(s)

Working adults ages 55-75 with access to retirement accounts or who have a 401k account. Especially interested in appealing to people who work for small businesses, local businesses, have company stock, and other unique needs in this space.

Industry/Entity Type

Financial services

Font styles to use
Other font styles liked:
• Cambria

Requirements
Must have
• Clear message & call to action
Nice to have
• Highlight how many Americans have been changing jobs since COVID and why it would be worth working with a professional to make decisions on what to do with retirement accounts and assets. (We're working on getting that stat)
Should not have
• Too much text, don't want to inundate with text blocks

```html
<!DOCTYPE html>
<html lang="en">
<head>
<meta charset="utf-8">
<title>Heronfield Wealth Advisors – Know That You Have Options</title>
<link href="https://fonts.googleapis.com/css2?family=Cinzel:wght@400;600&family=Arimo:wght@400;700&display=swap" rel="stylesheet">
<style>
  :root {
    --red: #c81d2b;
    --black: #0d0d0d;
    --ink: #1a1a1a;
    --white: #ffffff;
    --bg: #f4f4f4;
    --pro-row: #fbe9e6;
    --pro-row-alt: #f8e0dc;
    --con-row: #efefef;
    --con-row-alt: #e4e5e7;
    --muted: #9a9a9a;
  }
  * { box-sizing: border-box; margin: 0; padding: 0; }
  html, body { width: 1200px; height: 1200px; overflow: hidden; background: var(--bg); }
  body { font-family: "Arimo", Arial, sans-serif; color: var(--ink); position: relative; }

  .flyer {
    position: absolute; left: 0; top: 0;
    width: 1030px; height: 1332px;
    background: var(--white);
    transform-origin: 0 0;
    transform: translate(188px, 67px) scale(0.8);
    overflow: hidden;
  }

  .brand { position: absolute; left: 88px; top: 52px; display: flex; align-items: center; gap: 10px; }
  .brand-mark { width: 38px; height: 38px; background: var(--red); }
  .brand-name { font-family: "Cinzel", serif; font-size: 22px; font-weight: 600; color: var(--ink); letter-spacing: .5px; }

  .hero { position: absolute; left: 0; top: 123px; width: 1030px; height: 462px; overflow: hidden;
    background: linear-gradient(135deg, #1f2a22 0%, #2c372c 45%, #151a16 100%); }
  .hero-photo { position: absolute; inset: 0;
    background: linear-gradient(160deg, #7f8f6e 0%, #a59a7d 45%, #b4773f 70%, #d8cdb6 100%);
    clip-path: polygon(590px 0, 1030px 0, 1030px 462px, 530px 462px); }
  .hero-title { position: absolute; left: 93px; top: 88px; font-family: "Cinzel", serif; font-weight: 400;
    font-size: 60px; line-height: 57px; color: var(--white); }
  .hero-title .accent { color: var(--red); display: block; }
  .hero-lede { position: absolute; left: 92px; top: 306px; width: 360px; padding-left: 17px;
    border-left: 4px solid var(--red); font-size: 19.5px; line-height: 24px; color: var(--white); font-weight: 400; }

  .options { position: absolute; left: 90px; top: 612px; display: flex; gap: 41px; }
  .option { width: 180px; }
  .option h3 { font-size: 17px; color: var(--red); font-weight: 700; line-height: 20px; }
  .option h3 span { margin-right: 8px; }
  .option p { margin-top: 2px; border-left: 4px solid var(--red); padding-left: 17px; font-size: 13px; line-height: 16.2px; }

  .intro { position: absolute; left: 91px; top: 747px; width: 850px; font-size: 12.6px; line-height: 16px; }

  .compare-title { position: absolute; left: 0; width: 1030px; top: 879px; text-align: center;
    font-size: 19.5px; font-weight: 700; color: var(--red); }
  .compare-icon { position: absolute; left: 488px; top: 918px; }
  .compare { position: absolute; left: 137px; top: 946px; width: 751px; border-collapse: collapse; font-size: 14.5px; line-height: 18px; }
  .compare th { font-size: 18px; font-weight: 700; padding-bottom: 6px; text-align: center; }
  .compare th.pros { color: var(--red); width: 375px; }
  .compare th.cons { color: var(--ink); }
  .compare td { padding: 6px 9px; vertical-align: top; }
  .compare td.pro { background: var(--pro-row); }
  .compare td.con { background: var(--con-row); }
  .compare tr.alt td.pro { background: var(--pro-row-alt); }
  .compare tr.alt td.con { background: var(--con-row-alt); }
  .compare tr.row-1 td { height: 31px; }
  .compare tr.row-2 td, .compare tr.row-3 td { height: 50px; }
  .compare tr.row-3 td.pro { border-bottom: 4px solid var(--red); }
  .compare tr.row-3 td.con { border-bottom: 4px solid var(--black); }

  .footer-band { position: absolute; left: 0; top: 1183px; width: 1030px; height: 149px; background: var(--black); }
  .footer-cta { position: absolute; left: 0; top: 1169px; width: 262px; height: 163px; background: var(--red);
    clip-path: polygon(0 0, 262px 0, 238px 163px, 0 163px); }
  .footer-cta h2 { position: absolute; left: 90px; top: 44px; font-family: "Cinzel", serif; font-weight: 400;
    font-size: 30px; line-height: 36px; color: var(--white); }
  .footer-copy { position: absolute; left: 276px; top: 1220px; width: 410px; font-size: 11.2px; line-height: 15px; color: var(--muted); }
  .footer-contact { position: absolute; left: 730px; top: 1212px; color: var(--white); font-weight: 700; font-size: 13px; line-height: 15.5px; font-style: normal; }
  .footer-contact .phone { font-size: 19px; margin-bottom: 12px; }
</style>
</head>
<body>
  <article class="flyer">
    <header class="brand">
      <span class="brand-mark"></span>
      <span class="brand-name">Heronfield Wealth Advisors, Inc.</span>
    </header>

    <section class="hero">
      <div class="hero-photo" role="img" aria-label="Photo of a smiling retired couple walking together in a leafy greenhouse"></div>
      <h1 class="hero-title">Know That<span class="accent">You Have</span>Options</h1>
      <p class="hero-lede">The most important thing to realize when leaving an employer is that you have options for the money that you have worked hard for and saved.</p>
    </section>

    <section class="options">
      <div class="option"><h3><span>1</span>Leave it</h3><p>Most employer plans allow you to leave the funds within the qualified plan.</p></div>
      <div class="option"><h3><span>2</span>Roll it</h3><p>Depending on the type of qualified plan, you can roll the funds over from the employer plan to an IRA.</p></div>
      <div class="option"><h3><span>3</span>Move it</h3><p>If you’ve started working at a new company, they will often have their own qualified plan available that you can move your old company’s funds to.</p></div>
      <div class="option"><h3><span>4</span>Take it</h3><p>There is the option to take the account in cash, but it is not typically advisable due to the tax and potential penalty implications.</p></div>
    </section>

    <p class="intro">It is important to work with a fiduciary to help you evaluate your options and the pros and cons of them. A fiduciary is someone who is obligated to provide you unbiased advice and disclose any conflicts of interest in their recommendations. It can be particularly important to work with a fiduciary if you are retiring early or are generally confused about all of the information and misinformation out there.<br>We recommend working with an expert who has experience with a multitude of different types of qualified plans such as 401(k), 403(b), Employee Stock Ownership Plans, SEP IRAs, etc. Not all plan types are eligible for rollovers, and even if they are, they may vary in the types of plans that they can be rolled in to.</p>

    <h2 class="compare-title">Rolling over 401(k) assets to IRA</h2>
    <svg class="compare-icon" width="54" height="44" viewBox="0 0 54 44" aria-hidden="true">
      <circle cx="10" cy="10" r="8" fill="none" stroke="var(--red)" stroke-width="2.5"/>
      <path d="M6 10h8M10 6v8" stroke="var(--red)" stroke-width="2.5"/>
      <circle cx="42" cy="10" r="8" fill="none" stroke="var(--black)" stroke-width="2.5"/>
      <path d="M38 10h8" stroke="var(--black)" stroke-width="2.5"/>
      <path d="M10 20v5h32v-5M26 25v8M18 40l4-7h8l4 7zM4 41h46" fill="none" stroke="var(--black)" stroke-width="2.5"/>
    </svg>
    <table class="compare">
      <thead><tr><th class="pros">Pros</th><th class="cons">Cons</th></tr></thead>
      <tbody>
        <tr class="row-1"><td class="pro">Typically more investment choices in an IRA</td><td class="con">Less protection from creditors</td></tr>
        <tr class="row-2 alt"><td class="pro">Ability to make contributions to the account even after leaving your former employer</td><td class="con">Less access to funds prior to age 59½</td></tr>
        <tr class="row-3"><td class="pro">Choice of investment custodian and investment advisor you work with</td><td class="con">RMDs on funds at age 72 regardless if you are still working</td></tr>
      </tbody>
    </table>

    <footer>
      <div class="footer-band"></div>
      <div class="footer-cta"><h2>Talk to<br>us if</h2></div>
      <p class="footer-copy">You are changing jobs or retiring soon, hold company stock in your plan, own a small business, or are unsure which rollover path fits your goals. We will review your accounts, explain each choice in plain terms and help you decide.</p>
      <address class="footer-contact">
        <div class="phone">Call Us: 919-555-0178</div>
        Heronfield Wealth Advisors, Inc.<br>P.O. Box 40822<br>Millbrook, NC 27599
      </address>
    </footer>
  </article>
</body>
</html>
```